Business Card Design Project

I need a new business card design for my building/development company: Ridgewell Constructions.

We specialise in small sub-divisions, multi-story developments and new house builds.
We handle the whole process from concept stage right throught to a fully developed property.
Updates

Project Deadline Extended
Reason: Need a couple of extra days to decide as there are so many amazing designs

Target Market(s)

people looking to develop their property and need help. New property buyers

Industry/Entity Type

House

Requirements
Must have
• My logo on both sides:
Side 1: Logo taking up whole side as per old card but with a color/style change.

Side 2: Contact page: include logo but the rest just surprise me!

All contact details will be: (and need to be changable for each employee) I'll inform you of specifics before printing.

Name Surname
Position ie. Managing director
M: insert mobile
E: insert email
P.O. Box 518, Elmhurst, Vic, 3145
www.ridgewellconstructions.com.au

Nice to have
• Colors i'd like: (not necessarily all but this is the basic idea)

Black, blue, grey, silver, white

```html
<!DOCTYPE html>
<html lang="en">
<head>
<meta charset="utf-8">
<title>Ridgewell Constructions – Business Cards</title>
<link rel="stylesheet" href="https://fonts.googleapis.com/css2?family=Arimo:wght@400;700&family=Open+Sans:wght@400;600;700&display=swap">
<style>
  :root {
    --page-bg: #e9e9e9;
    --card-black: #050505;
    --card-white: #ffffff;
    --brand-blue: #1a8fd6;
    --text-dark: #1b1b1b;
    --text-light: #ffffff;
    --panel-tint: #edf2fa;
  }
  * { margin: 0; padding: 0; box-sizing: border-box; }
  html, body {
    width: 943px;
    height: 1200px;
    overflow: hidden;
    background: var(--page-bg);
    font-family: "Open Sans", Arial, sans-serif;
  }
  .canvas { position: relative; width: 943px; height: 1200px; }

  .card {
    position: absolute;
    left: 87px;
    width: 769px;
    height: 467px;
    overflow: hidden;
  }

  /* Front side */
  .card-front { top: 113px; background: var(--card-black); }
  .front-brand {
    position: absolute;
    left: 0; right: 0; top: 250px;
    display: flex;
    justify-content: center;
    align-items: center;
    gap: 16px;
  }
  .brand-mark {
    width: 34px; height: 34px;
    background: var(--brand-blue);
  }
  .front-name {
    font-size: 46px;
    font-weight: 700;
    color: var(--text-light);
    letter-spacing: -0.5px;
    line-height: 1;
    white-space: nowrap;
  }
  .front-tagline {
    position: absolute;
    left: 0; right: 0; top: 330px;
    text-align: center;
    font-size: 23px;
    font-weight: 600;
    color: var(--text-light);
  }

  /* Back side */
  .card-back {
    top: 638px;
    background: var(--card-white);
    font-family: "Arimo", Arial, sans-serif;
  }
  .back-brand {
    position: absolute;
    right: 48px; top: 136px;
    font-size: 25px;
    font-weight: 700;
    color: var(--brand-blue);
    white-space: nowrap;
  }
  .person { position: absolute; left: 83px; top: 140px; }
  .person-name {
    font-size: 23px;
    font-weight: 700;
    color: var(--brand-blue);
    line-height: 1.2;
    white-space: nowrap;
  }
  .person-role {
    font-size: 19px;
    color: var(--text-dark);
    line-height: 1.35;
  }
  .contact-panel {
    position: absolute;
    left: 0; top: 258px;
    width: 490px; height: 116px;
    background: var(--panel-tint);
    border-radius: 0 8px 8px 0;
    padding: 12px 0 0 83px;
  }
  .contact-line {
    font-size: 19px;
    color: var(--text-dark);
    line-height: 30px;
    white-space: nowrap;
  }
  .contact-line b { font-weight: 700; }
  .website {
    position: absolute;
    left: 0; right: 0; top: 408px;
    text-align: center;
    font-size: 26px;
    color: var(--brand-blue);
    white-space: nowrap;
  }
  .base-bar {
    position: absolute;
    left: 0; right: 0; bottom: 0;
    height: 14px;
    background: var(--brand-blue);
  }
</style>
</head>
<body>
<main class="canvas">
  <section class="card card-front" aria-label="Card front">
    <div class="front-brand">
      <span class="brand-mark"></span>
      <span class="front-name">Ridgewell Constructions</span>
    </div>
    <p class="front-tagline">renovation-construction-development</p>
  </section>

  <section class="card card-back" aria-label="Card back">
    <div class="back-brand">Ridgewell Constructions</div>
    <div class="person">
      <p class="person-name">Marcus Dalby</p>
      <p class="person-role">Director</p>
    </div>
    <div class="contact-panel">
      <p class="contact-line"><b>M</b>: 0400 555 218</p>
      <p class="contact-line"><b>E</b>: marcus@ridgewellconstructions.com.au</p>
      <p class="contact-line">P.O. Box 518, Elmhurst, Vic, 3145</p>
    </div>
    <p class="website">www.ridgewellconstructions.com.au</p>
    <div class="base-bar"></div>
  </section>
</main>
</body>
</html>
```